HollowPine Ventures Inc. Business Card Design

My business is custom renovations and homes.I would need to have a new business logo created to go along with my company name. The business card should be of a modern style as this is the market I am focused on. I would need my contact information and website posted on the card. I would also like to list a few of the tasks I conduct on the card (such as: Renovations, Additions, Repairs, New Homes, Design, Consultations). On the reverse of the card I currently have just my logo and my motto, "Shaping A Bold Path". However, I am open to completely changing everything as I am starting a new year and would like to excel further. Any new ideas and suggestions are always welcomed. Thank you.

Target Market(s)

Upscale residential and commercial renovations and builds

Industry/Entity Type

Business

Contact Information for Business Card

I would like the design to be able to be laser cut or burnt onto a wooden business card. I will be creating one option of cards for really loyal customers (wooden) and a second option for the everyday customer (paper).

Font styles to use
Other font styles liked:
• Calibri / anything of mordern taste

Colors
f37122
5c5c5c
474747
ffffff

Requirements
Must have
• I would like the colours of my business to be a sharp orange and grey. I believe this will symbolize a modern style. I am open to other suggestions if this is not suitable for the designers tastes. My contact info as follows:
• Will Marsh
• President
• HollowPine Ventures Inc.
• 555-214-3987
• will@hollowpineventures.example
• I would like my website (currently under construction) hollowpineventures.example on the card aswell.
Nice to have
• Along with a modern logo representing HollowPine, I would like something on the card besides the logo and contact information. Perhaps a small background design. I feel it may be nice to have my services listed on the card (in smaller font on the bottom) Renovations, Additions, Repairs, Design, Consultations.
Should not have
• The business card should not have too many different colors. Should not have rounded corners.

```html
<!DOCTYPE html>
<html lang="en">
<head>
<meta charset="utf-8">
<title>HollowPine Ventures Inc. – Business Cards</title>
<link rel="stylesheet" href="https://fonts.googleapis.com/css2?family=Carlito:wght@400;700&display=swap">
<style>
  :root {
    --orange: #f37122;
    --card: #2e2e2e;
    --card-edge: #262626;
    --grey-band: #5c5c5c;
    --grey-text: #a9a9a9;
    --light-band: #8a8a8a;
    --white: #ffffff;
    --stage: #3a3330;
  }
  * { box-sizing: border-box; margin: 0; padding: 0; }
  html, body { width: 1200px; height: 716px; overflow: hidden; }
  body {
    background: var(--stage);
    font-family: "Carlito", sans-serif;
    position: relative;
  }
  .card {
    position: absolute;
    width: 540px;
    height: 309px;
    top: 204px;
    background: linear-gradient(160deg, #363636 0%, var(--card) 55%, var(--card-edge) 100%);
    overflow: hidden;
  }
  .card--back { left: 40px; }
  .card--front { left: 620px; }

  /* Back card */
  .brand-block {
    position: absolute;
    left: 0; right: 0; top: 88px;
    text-align: center;
  }
  .brand-mark {
    color: var(--orange);
    font-weight: 700;
    font-size: 52px;
    line-height: 1;
    letter-spacing: 1px;
  }
  .brand-name {
    display: inline-block;
    margin-top: 10px;
    padding: 0 18px 4px;
    border-bottom: 1px solid var(--grey-band);
    color: var(--grey-text);
    font-size: 17px;
    letter-spacing: 4px;
  }
  .brand-motto {
    margin-top: 5px;
    color: var(--grey-text);
    font-size: 11px;
    letter-spacing: 2px;
  }

  /* Front card */
  .card--front .brand-block { top: 44px; left: 150px; right: 20px; }
  .card--front .brand-name { border-bottom: none; padding: 0; font-size: 15px; margin-top: 8px; }

  .holder {
    position: absolute;
    left: 26px; top: 168px;
    color: #d6d6d6;
    font-size: 16px;
  }
  .holder .role { font-size: 12px; color: var(--grey-text); }

  .accent-line {
    position: absolute;
    left: 0; right: 0; top: 190px;
    height: 2px;
    background: var(--orange);
  }
  .contact-band {
    position: absolute;
    left: 0; right: 0; top: 196px;
    height: 24px;
    background: var(--grey-band);
    display: flex;
    align-items: center;
    gap: 10px;
    padding: 0 14px;
    color: var(--white);
    font-size: 12.5px;
  }
  .contact-item { display: flex; align-items: center; gap: 5px; white-space: nowrap; }
  .contact-sep { color: #3b3b3b; font-size: 16px; }
  .icon { width: 12px; height: 12px; flex: none; }
  .icon-at { color: var(--orange); font-weight: 700; }

  .services {
    position: absolute;
    left: 0; right: 0; top: 234px;
    display: flex;
    justify-content: space-between;
    padding: 0 22px;
    list-style: none;
    color: #d0d0d0;
    font-size: 13px;
  }
  .services li { display: flex; align-items: center; gap: 5px; }
  .services li::before {
    content: "";
    width: 6px; height: 6px;
    background: var(--orange);
  }
  .motto-band {
    position: absolute;
    left: 0; right: 0; top: 266px;
    height: 16px;
    background: var(--light-band);
    color: #2b2b2b;
    font-size: 10px;
    letter-spacing: 9px;
    text-align: center;
    line-height: 16px;
  }
</style>
</head>
<body>

<section class="card card--back" aria-label="Card back">
  <div class="brand-block">
    <div class="brand-mark">HollowPine</div>
    <div class="brand-name">HollowPine Ventures Inc.</div>
    <div class="brand-motto">Shaping A Bold Path</div>
  </div>
</section>

<section class="card card--front" aria-label="Card front">
  <div class="brand-block">
    <div class="brand-mark">HollowPine</div>
    <div class="brand-name">HollowPine Ventures Inc.</div>
  </div>

  <div class="holder">Will Marsh <span class="role">- President</span></div>
  <div class="accent-line"></div>

  <div class="contact-band">
    <span class="contact-item"><span class="icon-at">@</span>hollowpineventures.example</span>
    <span class="contact-sep">/</span>
    <span class="contact-item">
      <svg class="icon" viewBox="0 0 12 12" aria-hidden="true"><path d="M3 1 L5 3.5 L4 5 Q5 7.5 7 8 L8.5 7 L11 9 L9.5 11 Q3 10.5 1 2.5 Z" fill="#f37122"/></svg>
      555-214-3987
    </span>
    <span class="contact-sep">/</span>
    <span class="contact-item">
      <svg class="icon" viewBox="0 0 12 12" aria-hidden="true"><rect x="0.75" y="2.25" width="10.5" height="7.5" fill="none" stroke="#f37122" stroke-width="1.3"/><path d="M1 2.5 L6 7 L11 2.5" fill="none" stroke="#f37122" stroke-width="1.3"/></svg>
      will@hollowpineventures.example
    </span>
  </div>

  <ul class="services">
    <li>Renovations</li>
    <li>Additions</li>
    <li>Repairs</li>
    <li>Design</li>
    <li>Consultations</li>
  </ul>

  <div class="motto-band">Shaping A Bold Path</div>
</section>

</body>
</html>
```